WPF Application Design

I require a design for a WPF application. I have the screenshots which needs to be redesigned for WPF application. Screens have different standard controls used, designer should suggest best placement and styling for the screens.

```html
<!DOCTYPE html>
<html lang="en">
<head>
<meta charset="utf-8">
<title>StepFlow – Course Template Manager</title>
<link href="https://fonts.googleapis.com/css2?family=Open+Sans:wght@400;600&display=swap" rel="stylesheet">
<style>
:root{
  --brand-red:#952b20;
  --brand-line:#c99a8e;
  --header-plum:#4b232d;
  --tab-light:#c6ab8f;
  --text-dark:#3b2a22;
  --text-light:#ffffff;
  --grid-row:#d0d0d0;
  --grid-line:#b49a7c;
  --input-bg:#e2e2e2;
  --radio-off:#7d7d7d;
  --radio-on:#111111;
}
*{box-sizing:border-box;margin:0;padding:0}
html,body{width:1200px;height:1001px;overflow:hidden}
body{font-family:"Open Sans",sans-serif;color:var(--text-dark);position:relative;background:#a98a6c}
.abs{position:absolute}
svg{display:block}
.title-bar{left:0;top:0;width:1200px;height:48px;background:var(--brand-red);border-bottom:1px solid var(--brand-line)}
.app-name{left:15px;top:13px;color:var(--text-light);font-size:19px;font-weight:400;white-space:nowrap}
.divider{left:103px;top:12px;width:2px;height:25px;background:#fff}
.ribbon{left:0;top:49px;width:1200px;height:63px;background:var(--brand-red)}
.ribbon-tab{top:7px;height:56px;width:130px;color:var(--text-light);font-size:15px;text-align:center}
.ribbon-tab.active{background:var(--tab-light);border-radius:8px 8px 0 0;color:var(--text-dark)}
.ribbon-tab span{position:absolute;left:0;right:0;bottom:2px}
.sub-nav{left:0;top:112px;width:1200px;height:34px;background:linear-gradient(90deg,#b9a181,#a88e6f 40%,#b9a88a 70%,#9d7f60);display:flex;align-items:center;padding-left:26px;font-size:14px;color:var(--text-dark);white-space:nowrap}
.sub-nav a{color:inherit;text-decoration:none;padding:0 8px 0 0}
.sub-nav a+a{border-left:1px solid #f2e8dc;padding-left:7px}
.side{left:0;top:146px;width:306px;height:855px;background:linear-gradient(90deg,#d8cab4,#b59c80 45%,#a78567)}
.side-gap{left:306px;top:146px;width:6px;height:855px;background:#c7b59b}
.panel-head{height:46px;background:var(--header-plum);color:var(--text-light);font-size:14px;display:flex;align-items:center;white-space:nowrap}
.main{left:312px;top:146px;width:888px;height:855px;background:linear-gradient(90deg,#aa8d71,#c9b8a0 45%,#cfc3ad 55%,#a98a6c 80%,#9b7a5b)}
.grid{left:312px;top:194px;width:888px}
.grid-head,.grid-row{display:grid;grid-template-columns:151px 198px 164px 116px 127px 132px}
.grid-head{height:34px;background:linear-gradient(90deg,#b9a285,#a88c6f);font-size:14px;color:var(--text-dark);white-space:nowrap}
.grid-head div{display:flex;align-items:center;padding-left:18px;border-right:2px solid #efe6da;overflow:hidden}
.grid-row{height:31px;background:var(--grid-row);border-bottom:2px solid var(--grid-line)}
.grid-row div{border-right:2px solid #efefef}
.tabs{left:316px;top:456px;width:884px;height:32px;background:linear-gradient(90deg,#a58a6e,#b49a7d 50%,#a3845f);font-size:14px;white-space:nowrap}
.tabs span{position:absolute;top:7px}
.tabs .current{top:0;height:32px;padding:7px 16px 0;background:#d9c9b7;color:#fff;border-radius:6px 6px 0 0}
.card{top:512px;height:425px;border-radius:9px}
.card.price{left:329px;width:409px;background:linear-gradient(90deg,#c4a796,#c8a99b 60%,#bf9f8a)}
.card.discount{left:753px;width:408px;background:linear-gradient(90deg,#e6dbd0,#c7ac9c 40%,#a8806a 70%,#a37a5c)}
.card-title{top:-10px;height:21px;background:rgba(190,160,148,.9);font-size:13px;padding:1px 6px;white-space:nowrap;line-height:19px}
.discount .card-title{background:#c8ada5;text-align:center}
.small{font-size:10px;white-space:nowrap}
.lbl{font-size:10px;white-space:nowrap}
.field{height:20px;background:var(--input-bg);border:1px solid #f4f4f4;font-size:10px;padding:2px 9px;line-height:15px}
.check{width:16px;height:16px;background:#d6d2c6;border:1px solid #a99d8b}
.dcheck{width:13px;height:13px;background:#f0f0f0;border:1px solid #999}
.radio{width:14px;height:14px;border-radius:50%;background:var(--radio-off)}
.radio.on{width:13px;height:13px;background:var(--radio-on);box-shadow:0 0 0 1.5px #e6e6e6}
.radio.soft{background:#8e8e8e}
</style>
</head>
<body>

<header class="abs title-bar">
  <div class="abs app-name">StepFlow</div>
  <div class="abs divider"></div>
  <svg class="abs" style="left:116px;top:11px" width="30" height="30" viewBox="0 0 30 30" aria-label="Save">
    <path d="M2 2h22l4 4v22H2z" fill="#fff"/><rect x="7" y="4" width="14" height="8" fill="#952b20"/><rect x="16" y="5" width="3" height="6" fill="#fff"/><rect x="6" y="17" width="18" height="9" fill="#952b20"/>
  </svg>
  <svg class="abs" style="left:152px;top:16px" width="30" height="18" viewBox="0 0 30 18" aria-label="Back"><path d="M0 9 12 0v5h18v8H12v5z" fill="#fff"/></svg>
  <svg class="abs" style="left:190px;top:16px" width="30" height="18" viewBox="0 0 30 18" aria-label="Forward"><path d="M30 9 18 0v5H0v8h18v5z" fill="#fff"/></svg>
  <svg class="abs" style="left:1118px;top:20px" width="66" height="18" viewBox="0 0 66 18" aria-label="Window controls">
    <path d="M2 16h18" stroke="#fff" stroke-width="1.6"/><rect x="29" y="1" width="15" height="15" fill="none" stroke="#fff" stroke-width="1.8"/><path d="M52 2l13 14M65 2 52 16" stroke="#fff" stroke-width="1.8"/>
  </svg>
</header>

<nav class="abs ribbon">
  <div class="abs ribbon-tab active" style="left:0">
    <svg class="abs" style="left:32px;top:5px" width="28" height="26" viewBox="0 0 28 26" aria-label="Home"><path d="M14 1 1 13h4v12h7v-8h4v8h7V13h4z" fill="#1c1c1c"/></svg>
    <span>Home</span>
  </div>
  <div class="abs ribbon-tab" style="left:100px;width:130px">
    <svg class="abs" style="left:44px;top:6px" width="30" height="30" viewBox="0 0 30 30" aria-label="Settings">
      <circle cx="12" cy="12" r="8" fill="none" stroke="#1c1c1c" stroke-width="4" stroke-dasharray="3 2.3"/><circle cx="12" cy="12" r="4" fill="none" stroke="#1c1c1c" stroke-width="2"/><circle cx="21" cy="21" r="5" fill="#952b20" stroke="#1c1c1c" stroke-width="2.5" stroke-dasharray="2 1.6"/>
    </svg>
    <span>Settings</span>
  </div>
</nav>

<div class="abs sub-nav">
  <a>Course Hierarchy Manager</a><a>Course Steps</a><a>Course Group</a><a>Course Template</a><a>Course Type</a>
</div>

<aside class="abs side"><div class="panel-head" style="padding-left:26px;margin-top:2px">Course Hierarchy Manager</div></aside>
<div class="abs side-gap"></div>

<main class="abs main">
  <div class="panel-head" style="justify-content:center;margin-top:2px">Course Template Manager</div>
</main>

<section class="abs grid">
  <div class="grid-head"><div>Template Number</div><div style="padding-left:22px">Template Name</div><div style="padding-left:29px">Number of Lessons</div><div style="padding-left:4px">Lesson Duration</div><div style="padding-left:5px">Created Date</div><div style="padding-left:18px;border:0">Modified Date</div></div>
  <div class="grid-row"><div></div><div></div><div></div><div></div><div></div><div></div></div>
  <div class="grid-row"><div></div><div></div><div></div><div></div><div></div><div></div></div>
  <div class="grid-row"><div></div><div></div><div></div><div></div><div></div><div></div></div>
  <div class="grid-row"><div></div><div></div><div></div><div></div><div></div><div></div></div>
  <div class="grid-row"><div></div><div></div><div></div><div></div><div></div><div></div></div>
  <div class="grid-row" style="border:0"><div></div><div></div><div></div><div></div><div></div><div></div></div>
</section>

<div class="abs tabs">
  <span style="left:14px">Template Type</span>
  <span style="left:140px">General</span>
  <span class="current" style="left:221px">Finance</span>
  <span style="left:313px">Preliminary Courses</span>
  <span style="left:501px">Packages</span>
  <span style="left:589px">Learning Goals</span>
  <span style="left:702px">Remarks</span>
</div>

<section class="abs card price">
  <div class="abs card-title" style="left:34px;width:124px">Price and Payment</div>
  <div class="abs small" style="left:340px;top:12px;color:#fff">Changeable</div>
  <div class="abs small" style="left:270px;top:28px;color:#fff">Discount Point</div>
  <div class="abs small" style="left:350px;top:28px;color:#fff">Yes</div>
  <div class="abs small" style="left:375px;top:28px;color:#fff">No</div>

  <div class="abs check" style="left:8px;top:45px"><svg width="14" height="14" viewBox="0 0 14 14"><path d="M3 7l3 3 5-7" stroke="#333" stroke-width="1.3" fill="none"/></svg></div>
  <div class="abs field" style="left:34px;top:43px;width:55px">1.00</div>
  <div class="abs lbl" style="left:93px;top:47px">CHF fixed price per course</div>
  <div class="abs field" style="left:272px;top:43px;width:51px">4.00</div>
  <div class="abs radio" style="left:350px;top:45px"></div>
  <div class="abs radio on" style="left:375px;top:45px"></div>

  <div class="abs check" style="left:8px;top:71px"><svg width="14" height="14" viewBox="0 0 14 14"><path d="M3 7l3 3 5-7" stroke="#333" stroke-width="1.3" fill="none"/></svg></div>
  <div class="abs field" style="left:34px;top:69px;width:55px">2.00</div>
  <div class="abs lbl" style="left:93px;top:72px">CHF Small class Charge</div>
  <div class="abs field" style="left:272px;top:69px;width:51px">4.00</div>
  <div class="abs radio on" style="left:350px;top:71px"></div>
  <div class="abs radio" style="left:375px;top:71px"></div>

  <div class="abs check" style="left:8px;top:95px"><svg width="14" height="14" viewBox="0 0 14 14"><path d="M3 7l3 3 5-7" stroke="#333" stroke-width="1.3" fill="none"/></svg></div>
  <div class="abs field" style="left:34px;top:93px;width:55px">3.00</div>
  <div class="abs lbl" style="left:93px;top:96px">CHF Individual acceptance on course</div>
  <div class="abs field" style="left:272px;top:93px;width:51px">4.00</div>
  <div class="abs radio" style="left:350px;top:95px"></div>
  <div class="abs radio on" style="left:375px;top:95px"></div>
</section>

<section class="abs card discount">
  <div class="abs card-title" style="left:31px;width:121px">Discount</div>
  <div class="abs small" style="left:342px;top:12px;color:#fff">Changeable</div>
  <div class="abs small" style="left:272px;top:28px;color:#fff">Discount in</div>
  <div class="abs small" style="left:348px;top:28px;color:#fff">Yes</div>
  <div class="abs small" style="left:378px;top:28px;color:#fff">No</div>

  <div class="abs lbl" style="left:10px;top:46px">Few Discount</div>
  <div class="abs field" style="left:155px;top:41px;width:44px"></div>
  <div class="abs radio soft" style="left:228px;top:43px"></div><div class="abs small" style="left:244px;top:43px;color:#fff">%</div>
  <div class="abs radio soft" style="left:260px;top:45px"></div><div class="abs small" style="left:277px;top:45px;color:#fff">Actual</div>
  <div class="abs dcheck" style="left:319px;top:46px"><svg width="11" height="11" viewBox="0 0 11 11"><path d="M2 5.5l2.5 2.5L9 2" stroke="#333" stroke-width="1.2" fill="none"/></svg></div>
  <div class="abs radio soft" style="left:352px;top:44px;opacity:.7"></div><div class="abs radio on" style="left:380px;top:45px"></div>

  <div class="abs lbl" style="left:10px;top:75px">Follow up course dicsount</div>
  <div class="abs field" style="left:155px;top:70px;width:44px"></div>
  <div class="abs radio soft" style="left:228px;top:72px"></div><div class="abs small" style="left:244px;top:72px;color:#fff">%</div>
  <div class="abs radio soft" style="left:260px;top:74px"></div><div class="abs small" style="left:277px;top:74px;color:#fff">Actual</div>
  <div class="abs dcheck" style="left:319px;top:75px"><svg width="11" height="11" viewBox="0 0 11 11"><path d="M2 5.5l2.5 2.5L9 2" stroke="#333" stroke-width="1.2" fill="none"/></svg></div>
  <div class="abs radio soft" style="left:352px;top:73px;opacity:.7"></div><div class="abs radio on" style="left:380px;top:74px"></div>

  <div class="abs lbl" style="left:10px;top:101px">Total Packet Discount</div>
  <div class="abs field" style="left:155px;top:96px;width:44px"></div>
  <div class="abs radio soft" style="left:228px;top:98px"></div><div class="abs small" style="left:244px;top:98px;color:#fff">%</div>
  <div class="abs radio soft" style="left:260px;top:100px"></div><div class="abs small" style="left:277px;top:100px;color:#fff">Actual</div>
  <div class="abs dcheck" style="left:319px;top:101px"><svg width="11" height="11" viewBox="0 0 11 11"><path d="M2 5.5l2.5 2.5L9 2" stroke="#333" stroke-width="1.2" fill="none"/></svg></div>
  <div class="abs radio soft" style="left:352px;top:99px;opacity:.7"></div><div class="abs radio on" style="left:380px;top:100px"></div>

  <div class="abs lbl" style="left:10px;top:129px">Few Discount</div>
  <div class="abs field" style="left:155px;top:124px;width:44px"></div>
  <div class="abs radio soft" style="left:228px;top:126px"></div><div class="abs small" style="left:244px;top:126px;color:#fff">%</div>
  <div class="abs radio soft" style="left:260px;top:128px"></div><div class="abs small" style="left:277px;top:128px;color:#fff">Actual</div>
  <div class="abs dcheck" style="left:319px;top:129px"><svg width="11" height="11" viewBox="0 0 11 11"><path d="M2 5.5l2.5 2.5L9 2" stroke="#333" stroke-width="1.2" fill="none"/></svg></div>
  <div class="abs radio soft" style="left:352px;top:127px;opacity:.7"></div><div class="abs radio on" style="left:380px;top:128px"></div>

  <div class="abs lbl" style="left:10px;top:158px">Few Discount</div>
  <div class="abs field" style="left:155px;top:153px;width:44px"></div>
  <div class="abs radio soft" style="left:228px;top:155px"></div><div class="abs small" style="left:244px;top:155px;color:#fff">%</div>
  <div class="abs radio soft" style="left:260px;top:157px"></div><div class="abs small" style="left:277px;top:157px;color:#fff">Actual</div>
  <div class="abs dcheck" style="left:319px;top:158px"><svg width="11" height="11" viewBox="0 0 11 11"><path d="M2 5.5l2.5 2.5L9 2" stroke="#333" stroke-width="1.2" fill="none"/></svg></div>
  <div class="abs radio soft" style="left:352px;top:156px;opacity:.7"></div><div class="abs radio on" style="left:380px;top:157px"></div>
</section>

</body>
</html>
```